Company or website name
- Harwood & Beale LLP
- Links to the website
- harwoodbeale-example.com
- Describe your company and organization and target audience
- lawyers and clients in the need of lawyer for defective products etc
- The design should have the following
- yes
- Other Facts

```html
<!DOCTYPE html>
<html lang="en">
<head>
<meta charset="utf-8">
<title>Harwood &amp; Beale LLP</title>
<link href="https://fonts.googleapis.com/css2?family=Open+Sans:wght@400;600&family=Arimo:wght@400&family=PT+Serif&family=Oswald:wght@600&display=swap" rel="stylesheet">
<style>
:root{
  --blue:#1c86c6;
  --blue-dark:#0f5f98;
  --blue-deep:#0b4f84;
  --cyan:#0a97d6;
  --page:#e5e5e1;
  --white:#ffffff;
  --ink:#222;
  --text:#3a3a3a;
  --grey-band:#3b3b3b;
  --partner:#e9e9e9;
  --badge:#b9b9b9;
}
*{margin:0;padding:0;box-sizing:border-box}
html,body{width:997px;height:1200px;overflow:hidden}
body{position:relative;background:var(--page);font-family:"Arimo",Arial,sans-serif;color:var(--text)}
.abs{position:absolute}
.header{left:0;top:0;width:997px;height:133px;background:linear-gradient(#1e8fd0,#1a78b6 70%,#166aa3);border-top:5px solid #1a6ea8}
.header-rule{left:0;top:133px;width:997px;height:11px;background:var(--white)}
.brand{left:80px;top:26px;display:flex;align-items:center;gap:10px}
.brand-mark{width:42px;height:42px;border-radius:50%;background:#bfe9fb}
.brand-name{font-family:"Open Sans",Arial,sans-serif;font-weight:600;font-size:27px;color:var(--white);letter-spacing:-.3px}
.nav{left:410px;top:28px;width:496px;height:40px;background:linear-gradient(#fff,#e6e6e6);border-radius:3px;box-shadow:0 2px 3px rgba(0,0,0,.3);display:flex;align-items:center;padding-left:18px}
.nav a{font-family:"PT Serif",Georgia,serif;font-size:14px;color:#444;text-decoration:none;padding:0 12px;border-left:1px solid #c7c7c7;line-height:16px}
.nav a:first-child{border-left:none}
.nav-shadow{left:420px;top:68px;width:476px;height:18px}
.panel{left:91px;top:103px;width:815px;height:1037px;background:var(--white);box-shadow:0 0 6px rgba(0,0,0,.35)}
.hero{left:100px;top:111px;width:797px;height:390px;background:linear-gradient(90deg,#141414,#2a2a2a 45%,#3b3b3b 70%,#1e2430)}
.hero-title{left:150px;top:326px;font-family:"Open Sans",Arial,sans-serif;font-size:31px;color:var(--white);font-weight:400;letter-spacing:.5px}
.hero-text{left:150px;top:366px;width:342px;font-family:"Open Sans",Arial,sans-serif;font-size:14.5px;line-height:19px;color:#eee;text-align:justify}
.arrow{top:270px;width:26px;height:40px;background:var(--blue)}
.hero-shadow{left:120px;top:501px;width:757px;height:20px}
.section-title{left:105px;top:529px;font-family:"Oswald",Impact,sans-serif;font-weight:600;font-size:21px;color:var(--ink);letter-spacing:.5px}
.intro{left:105px;top:563px;width:533px;font-size:12px;line-height:18.3px;color:#333}
.intro p+p{margin-top:18.3px}
.intro-photo{left:656px;top:567px;width:231px;height:144px;background:linear-gradient(135deg,#7c8e7b,#b9c9d6 55%,#5d6e80)}
.card{top:753px;width:248px;height:247px;border:1px solid #cfcfcf;background:#efefef}
.card-top{position:absolute;right:-1px;top:-1px;width:145px;height:6px;background:var(--cyan)}
.card-bottom{position:absolute;left:-1px;bottom:-1px;width:118px;height:7px;background:var(--cyan)}
.card h3{position:absolute;left:15px;top:16px;font-weight:400;font-size:18px;color:#444;font-family:"Open Sans",Arial,sans-serif;letter-spacing:-.3px}
.card-img{position:absolute;left:15px;top:47px;width:218px;height:98px}
.card p{position:absolute;left:17px;top:151px;width:216px;font-size:11px;line-height:16.6px;text-align:justify;color:#555}
.more{position:absolute;left:162px;top:218px;width:71px;height:22px;background:var(--blue-deep);color:#fff;font-size:10px;line-height:22px;text-align:center;text-decoration:none;box-shadow:0 0 0 1px #6aa7d4 inset}
.card-shadow{top:1000px;width:170px;height:16px}
.partner-band{left:0;top:1048px;width:997px;height:105px;background:var(--grey-band)}
.partners{left:91px;top:1050px;width:815px;height:88px;background:var(--partner);display:flex;align-items:center;justify-content:space-around;padding:0 30px}
.badge{background:var(--badge);border-radius:4px;height:30px}
.footer{left:0;top:1153px;width:997px;height:47px;background:var(--blue-dark)}
.copyright{left:93px;top:1170px;font-size:11.5px;color:#fff}
.follow{left:714px;top:1168px;font-family:"Oswald",Impact,sans-serif;font-size:13px;color:#fff;letter-spacing:.3px}
.social{top:1166px;width:22px;height:22px;border:2px solid #fff;border-radius:50%}
</style>
</head>
<body>
<div class="abs header"></div>
<div class="abs header-rule"></div>

<div class="abs brand">
  <span class="brand-mark"></span>
  <span class="brand-name">Harwood &amp; Beale LLP</span>
</div>

<nav class="abs nav">
  <a href="#">HOME</a><a href="#">ABOUT US</a><a href="#">SOLUTIONS</a><a href="#">SERVICES</a><a href="#">CONTACT US</a>
</nav>
<svg class="abs nav-shadow" viewBox="0 0 476 18" preserveAspectRatio="none"><path d="M0 0 Q238 26 476 0 Q238 12 0 0Z" fill="#0d4e7e" opacity=".8"/></svg>

<div class="abs panel"></div>

<div class="abs hero" role="img" aria-label="Night city skyline with a businesswoman standing with folded arms"></div>
<h1 class="abs hero-title">HARWOOD &amp; BEALE LLP</h1>
<p class="abs hero-text">Lorem ipsum dolor sit amet, consectetuer adipiscing elit, sed diam nonummy nibh euismod tincidunt ut laoreet dolore magna.</p>
<div class="abs arrow" style="left:100px"><svg width="26" height="40"><path d="M16 12 L9 20 L16 28" stroke="#fff" stroke-width="3.5" fill="none"/></svg></div>
<div class="abs arrow" style="left:870px"><svg width="26" height="40"><path d="M10 12 L17 20 L10 28" stroke="#fff" stroke-width="3.5" fill="none"/></svg></div>
<svg class="abs hero-shadow" viewBox="0 0 757 20" preserveAspectRatio="none"><path d="M0 20 Q30 0 120 0 L637 0 Q727 0 757 20 Q380 -4 0 20Z" fill="#333" opacity=".55"/></svg>

<h2 class="abs section-title">WHO WE ARE</h2>
<div class="abs intro">
  <p>Lorem ipsum dolor sit amet, consectetuer adipiscing elit, sed diam nonummy nibh euismod tincidunt ut laoreet dolore magna aliquam erat volutpat. Ut wisi enim ad minim veniam, quis nostrud exerci tation ullamcorper suscipit lobortis nisl ut aliquip ex ea commodo consequat. Duis autem vel eum iriure dolor in hendrerit in vulputate velit esse molestie consequat, vel illum dolore eu feugiat nulla facilisis at vero eros et accumsan et iusto odio dignissim qui blandit praesent luptatum zzril delenit augue duis dolore te feugait nulla facilisi.</p>
  <p>Nam liber tempor cum soluta nobis eleifend option congue nihil imperdiet doming id quod mazim placerat facer possim assum.</p>
</div>
<div class="abs intro-photo" role="img" aria-label="Businessman in a blue shirt seated outdoors near an office building"></div>

<article class="abs card" style="left:108px">
  <span class="card-top"></span><span class="card-bottom"></span>
  <h3>Heading goes here</h3>
  <div class="card-img" role="img" aria-label="Hand touching a glowing digital interface" style="background:linear-gradient(135deg,#2a2a2a,#555 50%,#3a3a3a)"></div>
  <p>Lorem ipsum dolor sit amet, consectetuer adipiscing elit, sed diam nonummy nibh euismod tincidunt ut laoreet dolore magna aliquam erat volutpat.</p>
  <a class="more" href="#">» Read More</a>
</article>
<article class="abs card" style="left:375px">
  <span class="card-top"></span><span class="card-bottom"></span>
  <h3>Heading goes here</h3>
  <div class="card-img" role="img" aria-label="Silhouettes of business people over a blue world map" style="background:linear-gradient(135deg,#0a6fd0,#25c7f0 50%,#0a5db8)"></div>
  <p>Lorem ipsum dolor sit amet, consectetuer adipiscing elit, sed diam nonummy nibh euismod tincidunt ut laoreet dolore magna aliquam erat volutpat.</p>
  <a class="more" href="#">» Read More</a>
</article>
<article class="abs card" style="left:640px">
  <span class="card-top"></span><span class="card-bottom"></span>
  <h3>Heading goes here</h3>
  <div class="card-img" role="img" aria-label="Group of business people in conversation" style="background:linear-gradient(135deg,#6a5a4e,#9a8a7e 50%,#3e3a3a)"></div>
  <p>Lorem ipsum dolor sit amet, consectetuer adipiscing elit, sed diam nonummy nibh euismod tincidunt ut laoreet dolore magna aliquam erat volutpat.</p>
  <a class="more" href="#">» Read More</a>
</article>
<svg class="abs card-shadow" style="left:186px" viewBox="0 0 170 16" preserveAspectRatio="none"><path d="M0 16 Q20 0 170 0 Q60 2 0 16Z" fill="#333" opacity=".5"/></svg>
<svg class="abs card-shadow" style="left:453px" viewBox="0 0 170 16" preserveAspectRatio="none"><path d="M0 16 Q20 0 170 0 Q60 2 0 16Z" fill="#333" opacity=".5"/></svg>
<svg class="abs card-shadow" style="left:718px" viewBox="0 0 170 16" preserveAspectRatio="none"><path d="M0 16 Q20 0 170 0 Q60 2 0 16Z" fill="#333" opacity=".5"/></svg>

<div class="abs partner-band"></div>
<div class="abs partners" aria-label="Partner companies">
  <span class="badge" style="width:70px;height:44px"></span>
  <span class="badge" style="width:55px;height:36px;border-radius:50%"></span>
  <span class="badge" style="width:125px"></span>
  <span class="badge" style="width:62px;height:20px"></span>
  <span class="badge" style="width:105px;height:24px"></span>
  <span class="badge" style="width:128px;height:38px"></span>
  <span class="badge" style="width:75px;height:20px"></span>
</div>

<footer class="abs footer"></footer>
<p class="abs copyright">© Copyright 2014. All rights reserved.</p>
<span class="abs follow">FOLLOW US</span>
<span class="abs social" style="left:778px"></span>
<span class="abs social" style="left:822px"></span>
<span class="abs social" style="left:866px"></span>
</body>
</html>
```